New Update: I am changing the title of the book and the back cover text. Title was too long before. Same style as before.
New Title: Under the Quiet Sky
New Subtitle: A Gardener’s Notes on Patience (italics on front cover)

Back cover text:
Under the Quiet Sky: A Gardener’s Notes on Patience offers clear, compassionate guidance for those recovering from total loss. Drawing from his experience as a Brennick Flood survivor, Tobias Quellhorst shares practical advice on insurance, rebuilding, and emotional healing, along with lessons in strength and community. This is not a book about tragedy; it’s about perseverance and renewal. Under the Quiet Sky is a trusted companion for anyone rebuilding life, home, and hope after disaster.

Font styles to use
Serif

Colors
EB3D1F
EC4F4E
F09395
F8D3D4
FCEDEE

Requirements
Should not have
• No pictures or anything related to fire on the cover.

```html
<!DOCTYPE html>
<html lang="en">
<head>
<meta charset="utf-8">
<title>Under the Quiet Sky – Book Cover</title>
<link rel="stylesheet" href="https://fonts.googleapis.com/css2?family=Playfair+Display:ital,wght@0,700;0,800;0,900;1,700&family=Lora:ital,wght@0,400;0,500;1,400&display=swap">
<style>
  :root {
    --flame: #eb3d1f;
    --coral: #ec4f4e;
    --rose: #f09395;
    --blush: #f8d3d4;
    --petal: #fcedee;
    --panel-deep: rgba(235, 61, 31, 0.78);
    --panel-soft: rgba(236, 79, 78, 0.5);
    --photo-tone: #3a2226;
    --white: #ffffff;
    --ink: #1a0d0d;
  }
  * { margin: 0; padding: 0; box-sizing: border-box; }
  html, body { width: 1200px; height: 859px; overflow: hidden; }
  body {
    position: relative;
    background: radial-gradient(ellipse 62% 72% at 50% 50%, var(--rose) 0%, var(--coral) 55%, var(--flame) 100%);
    font-family: "Lora", serif;
  }

  /* Back cover */
  .back-panel {
    position: absolute; left: 79px; top: 82px; width: 425px; height: 625px;
    border-radius: 16px;
    background: linear-gradient(120deg, var(--panel-deep) 0%, var(--panel-soft) 55%, rgba(235, 61, 31, 0.65) 100%);
  }
  .author-photo {
    position: absolute; left: 178px; top: 40px; width: 232px; height: 235px;
    border-radius: 60px 60px 8px 8px;
    background: linear-gradient(180deg, #8a6a62 0%, #4a3034 35%, var(--photo-tone) 100%);
  }
  .photo-frame {
    position: absolute; left: 167px; top: 107px; width: 254px; height: 172px;
    border: 4px solid var(--white); border-radius: 16px;
  }
  .back-name {
    position: absolute; left: 79px; top: 280px; width: 430px; text-align: center;
    font-family: "Playfair Display", serif; font-weight: 900; font-size: 24px;
    letter-spacing: 0.2px; color: var(--white);
  }
  .back-copy {
    position: absolute; left: 117px; top: 324px; width: 360px;
    font-weight: 400; font-size: 15.6px; line-height: 26.4px; color: var(--white);
  }
  .back-copy p + p { margin-top: 26.4px; }

  /* Spine */
  .spine {
    position: absolute; left: 589px; top: 84px;
    writing-mode: vertical-rl; color: var(--ink);
    display: flex; gap: 32px; align-items: center;
  }
  .spine-title { font-family: "Playfair Display", serif; font-weight: 700; font-size: 15px; letter-spacing: 0.2px; }
  .spine-author { font-weight: 400; font-size: 19px; }

  /* Front cover */
  .front-title {
    position: absolute; left: 662px; top: 62px;
    font-family: "Playfair Display", serif;
    font-weight: 800; font-size: 104px; line-height: 103px; letter-spacing: -1px;
    background: linear-gradient(95deg, var(--petal) 0%, var(--white) 45%, var(--blush) 100%);
    -webkit-background-clip: text; background-clip: text; color: transparent;
  }
  .front-subtitle {
    position: absolute; left: 668px; top: 488px;
    font-family: "Playfair Display", serif; font-style: italic; font-weight: 700;
    font-size: 35px; line-height: 42px; color: var(--ink);
  }
  .front-tagline {
    position: absolute; left: 668px; top: 590px;
    font-weight: 400; font-size: 25px; line-height: 28px; color: var(--white);
  }
  .front-author {
    position: absolute; left: 741px; top: 762px;
    font-family: "Playfair Display", serif; font-weight: 900; font-size: 30px; letter-spacing: 0.3px;
    background: linear-gradient(180deg, var(--white) 0%, var(--blush) 100%);
    -webkit-background-clip: text; background-clip: text; color: transparent;
  }
</style>
</head>
<body>
  <section class="back-cover">
    <div class="back-panel"></div>
    <div class="author-photo" role="img" aria-label="Portrait photograph of the author"></div>
    <div class="photo-frame"></div>
    <h2 class="back-name">TOBIAS QUELLHORST</h2>
    <div class="back-copy">
      <p><em>Under the Quiet Sky: A Gardener’s Notes on Patience</em> offers clear, compassionate guidance for those recovering from total loss. Drawing from his experience as a Brennick Flood survivor, Tobias Quellhorst shares practical advice on insurance, rebuilding, and emotional healing, along with lessons in strength and community.</p>
      <p>This is not a book about tragedy; it’s about perseverance and renewal. <em>Under the Quiet Sky</em> is a trusted companion for anyone rebuilding life, home, and hope after disaster.</p>
    </div>
  </section>

  <section class="spine">
    <span class="spine-title">UNDER THE QUIET SKY: A GARDENER’S NOTES ON PATIENCE</span>
    <span class="spine-author">Tobias Quellhorst</span>
  </section>

  <section class="front-cover">
    <h1 class="front-title">UNDER<br>THE<br>QUIET<br>SKY</h1>
    <p class="front-subtitle">A Gardener’s Notes<br>on Patience</p>
    <p class="front-tagline">A Journey<br>Through Loss,<br>Recovery,<br>and Rebuilding</p>
    <p class="front-author">TOBIAS QUELLHORST</p>
  </section>
</body>
</html>
```